Creative/innovative law firm website

A law firm website that immediately looks different from other law firm websites. We like the color scheme (dark background with warm, neutral colors) and simple, organic logos (trees, leaves, etc.) of this website: https://nimbleway.law/

We'll be offering creative/innovative solutions to complex problems faced by state governments, industries, other law firms, and individuals. We're located in Montana (U.S.A.), and the outdoors is a huge part of our lives and identities.

We will need a home page, an "About Us" page with a separate subpage for each attorney (two attorneys), a blog or "Publications" page, a payment portal (which will integrate with Quindle), and a "Services" page.

```html
<!DOCTYPE html>
<html lang="en">
<head>
<meta charset="utf-8">
<title>Innovative Law Solutions</title>
<link href="https://fonts.googleapis.com/css2?family=Jost:ital,wght@0,300;0,400;0,500;0,600;1,300;1,400&family=Josefin+Sans:wght@600;700&display=swap" rel="stylesheet">
<style>
:root{
  --bg-dark:#2b2b2b;
  --bg-mid:#3f3f3f;
  --bg-card:#3a3a3a;
  --black:#141414;
  --tan:#d9c3a5;
  --copper:#c8874a;
  --accent:#e09a3c;
  --text:#d6d2cc;
  --muted:#b3aea7;
  --white:#ffffff;
}
*{margin:0;padding:0;box-sizing:border-box}
html,body{width:1200px;height:4792px;overflow:hidden;background:var(--bg-dark)}
body{position:relative;font-family:'Jost',sans-serif;color:var(--text)}
.abs{position:absolute}
.heading{position:absolute;font-family:'Jost',sans-serif;font-weight:300;font-size:56px;color:var(--tan);letter-spacing:1px;line-height:1}
.para{position:absolute;font-size:19px;line-height:24px;color:var(--muted);font-weight:300}

/* header / hero */
.hero{left:0;top:0;width:1200px;height:735px;background:radial-gradient(ellipse at 30% 35%,#6a4a22 0%,#3b2e20 22%,#252322 50%,#2b2b2b 100%)}
.hero-photo{left:0;top:0;width:1200px;height:735px;background:linear-gradient(180deg,rgba(0,0,0,0) 60%,var(--bg-dark) 100%),radial-gradient(circle at 420px 320px,#f3e7b0 0,#c9892f 40px,rgba(120,70,20,.55) 170px,rgba(0,0,0,0) 320px),radial-gradient(circle at 950px 110px,#f0b050 0,rgba(240,170,70,0) 40px)}
.logo{left:58px;top:44px;font-family:'Josefin Sans',sans-serif;font-weight:600;font-size:20px;color:var(--white);letter-spacing:1.5px}
.nav{left:307px;top:46px;display:flex;gap:0;font-size:13px;font-weight:500;letter-spacing:1px;color:var(--white)}
.nav a{color:inherit;text-decoration:none;position:absolute;white-space:nowrap}
.nav .active::after{content:"";position:absolute;left:0;right:0;bottom:-8px;height:2px;background:var(--accent)}
.nav .portal{color:var(--accent);text-decoration:underline}
.btn-consult{left:921px;top:33px;width:214px;height:38px;border:2px solid var(--accent);border-radius:19px;color:var(--accent);font-size:12px;font-weight:500;letter-spacing:.8px;display:flex;align-items:center;justify-content:center}
.hero-title{left:707px;top:338px;font-family:'Josefin Sans',sans-serif;font-weight:700;font-size:50px;line-height:58px;color:var(--white);letter-spacing:1px}

/* who we are */
.feature{position:absolute;width:250px}
.feature svg{display:block}
.feature h3{font-size:22px;font-weight:500;letter-spacing:2px;color:var(--white);margin-top:22px}
.feature p{font-size:13px;line-height:16px;color:var(--muted);margin-top:12px;font-weight:300}
.who-photo{left:725px;top:800px;width:475px;height:578px;background:linear-gradient(160deg,#cfd6d8 0%,#8e8f8a 45%,#5f564e 75%,#e8e6e2 100%)}
.frame-copper{left:701px;top:898px;width:499px;height:519px;border-left:2px solid var(--copper);border-bottom:2px solid var(--copper);border-top:2px solid var(--copper)}

/* why choose */
.why{left:0;top:1587px;width:1200px;height:753px;background:var(--bg-mid)}
.why-photo-a{left:45px;top:1694px;width:279px;height:378px;background:linear-gradient(150deg,#d9dee0 0%,#9aa2a5 50%,#5d5a55 100%)}
.why-frame{left:166px;top:1752px;width:433px;height:463px;border-left:2px solid #e6e6e6;border-top:2px solid #e6e6e6;border-bottom:2px solid #e6e6e6}
.why-photo-b{left:199px;top:1784px;width:435px;height:465px;background:linear-gradient(150deg,#c9c2b8 0%,#3c4e6e 45%,#23304a 70%,#b07a45 100%)}
.btn-outline{left:696px;top:2094px;width:134px;height:40px;border:2px solid var(--copper);border-radius:20px;color:var(--copper);font-size:12px;font-weight:500;letter-spacing:.5px;display:flex;align-items:center;justify-content:center}

/* solutions */
.sol-card{position:absolute;top:2732px;width:251px;height:346px}
.sol-caption{position:absolute;left:34px;right:0;bottom:0;height:148px;background:var(--bg-card);padding:38px 22px 0 22px}
.sol-caption h4{font-size:19px;font-weight:500;color:var(--white);line-height:22px}
.sol-caption p{font-size:12px;line-height:15px;color:var(--muted);margin-top:10px;font-weight:300}
.sol-big{left:725px;top:2544px;width:343px;height:534px;background:linear-gradient(160deg,#9fb3b3 0%,#4f7679 45%,#2d4f56 75%,#6b5a4a 100%)}
.sol-big .sol-caption{left:28px;height:148px}

/* testimonials */
.quote{position:absolute;width:300px}
.quote .mark{font-family:'Josefin Sans',sans-serif;font-weight:700;font-size:110px;line-height:70px;color:var(--copper);height:62px;overflow:hidden}
.quote p{font-style:italic;font-weight:300;font-size:19px;line-height:24px;color:var(--text);margin-top:24px}
.quote .name{font-weight:600;font-size:20px;color:var(--copper);margin-top:20px}

/* contact */
.contact-scene{left:0;top:4060px;width:1200px;height:478px;background:linear-gradient(180deg,var(--bg-dark) 0%,#3a3a36 30%,#4a4f48 55%,#2c3a28 80%,#1f2a1c 100%)}
.field{position:absolute;height:41px;border:1.5px solid var(--tan);border-radius:21px;padding:0 20px;font-size:17px;color:var(--white);display:flex;align-items:center}
.field.msg{align-items:flex-start;padding-top:14px;border-radius:24px}
.btn-submit{left:519px;top:4308px;width:160px;height:48px;background:var(--copper);border-radius:24px;color:var(--white);font-size:17px;font-weight:600;letter-spacing:1px;display:flex;align-items:center;justify-content:center}
.location{left:385px;top:4444px;display:flex;align-items:center;gap:14px;font-family:'Josefin Sans',sans-serif;font-weight:700;font-size:19px;color:var(--white);text-decoration:underline}

/* footer */
.footer{left:0;top:4538px;width:1200px;height:172px;background:var(--black)}
.info{position:absolute;top:4600px;display:flex;align-items:center;gap:16px;font-size:17px;line-height:21px;color:var(--text)}
.info .dot{width:38px;height:38px;border-radius:50%;background:var(--tan);display:flex;align-items:center;justify-content:center}
.bottom-bar{left:0;top:4710px;width:1200px;height:82px;background:var(--bg-dark)}
.copyright{left:132px;top:4742px;font-size:14px;letter-spacing:2.5px;color:var(--text)}
.payment{left:893px;top:4736px;display:flex;align-items:center;gap:14px;font-size:14px;letter-spacing:2.5px;color:var(--text)}
.payment strong{font-size:24px;letter-spacing:0;font-weight:600;color:var(--white)}
</style>
</head>
<body>

<header>
  <div class="abs hero"></div>
  <div class="abs hero-photo" role="img" aria-label="Hand shielding a glowing light bulb above a tablet with golden network lines"></div>
  <div class="abs logo">COMPANY LOGO</div>
  <nav class="abs nav">
    <a class="active" style="left:0">HOME</a>
    <a style="left:82px">ABOUT US</a>
    <a style="left:193px">SERVICES</a>
    <a style="left:301px">PUBLICATIONS</a>
    <a class="portal" style="left:444px">PAYMENT PORTAL</a>
  </nav>
  <div class="abs btn-consult">CONSULTATION REQUEST</div>
  <h1 class="abs hero-title">INNOVATIVE LAW<br>SOLUTIONS</h1>
</header>

<section class="who">
  <h2 class="heading" style="left:128px;top:836px">WHO WE ARE</h2>
  <p class="para" style="left:130px;top:921px;width:520px">Lorem ipsum dolor sit amet, consectetur adipiscing elit, sed do eiusmod tempor incididunt ut labore et dolore maorem ipsum dolor sit amet, consectetur adipiscing elit, sed do eiusmod tempor incididunt ut labore et dolore ma</p>

  <div class="feature" style="left:130px;top:1051px">
    <svg width="48" height="54" viewBox="0 0 48 54" fill="none" stroke="#c8874a" stroke-width="2"><path d="M24 50V18M24 30l-8-7M24 36l8-8"/><path d="M14 38c-8-1-12-9-8-15 0-8 7-13 14-12 3-6 12-6 15 0 7 1 11 8 8 14 3 7-3 14-11 13"/></svg>
    <h3>Lorem Ipsum</h3>
    <p>Lorem ipsum dolor sit amet, consectetur adipiscing elit, sed do eiusmod tempor incididunt ut labore et dolore ma</p>
  </div>
  <div class="feature" style="left:419px;top:1051px">
    <svg width="60" height="54" viewBox="0 0 60 54" fill="none" stroke="#c8874a" stroke-width="2"><path d="M8 50C10 20 30 6 56 4c0 26-14 44-42 40"/><path d="M8 50C20 34 32 24 46 16"/></svg>
    <h3>Lorem Ipsum</h3>
    <p>Lorem ipsum dolor sit amet, consectetur adipiscing elit, sed do eiusmod tempor incididunt ut labore et dolore ma</p>
  </div>
  <div class="feature" style="left:130px;top:1255px">
    <svg width="48" height="54" viewBox="0 0 48 54" fill="none" stroke="#c8874a" stroke-width="2"><circle cx="24" cy="32" r="18"/><path d="M24 14V4M24 10c-6-6-12-4-12-4M24 10c6-6 12-4 12-4M16 26h16M13 34h22M16 42h16"/></svg>
    <h3>Lorem Ipsum</h3>
    <p>Lorem ipsum dolor sit amet, consectetur adipiscing elit, sed do eiusmod tempor incididunt ut labore et dolore ma</p>
  </div>
  <div class="feature" style="left:419px;top:1255px">
    <svg width="62" height="54" viewBox="0 0 62 54" fill="none" stroke="#c8874a" stroke-width="2"><path d="M31 50C12 48 4 30 10 12c10 2 18 10 21 22 3-12 11-20 21-22 6 18-2 36-21 38z"/><path d="M31 50V30M22 20l9 14M44 12L31 34"/></svg>
    <h3>Lorem Ipsum</h3>
    <p>Lorem ipsum dolor sit amet, consectetur adipiscing elit, sed do eiusmod tempor incididunt ut labore et dolore ma</p>
  </div>

  <div class="abs frame-copper"></div>
  <div class="abs who-photo" role="img" aria-label="Three colleagues discussing work around a laptop in a bright office"></div>
</section>

<section>
  <div class="abs why"></div>
  <div class="abs why-photo-a" role="img" aria-label="Attorney smiling at a meeting table"></div>
  <svg class="abs" style="left:378px;top:1674px" width="290" height="282" viewBox="0 0 290 282" fill="#d9c3a5">
    <pattern id="dotGrid" width="19" height="19" patternUnits="userSpaceOnUse"><circle cx="2" cy="2" r="1.8"/></pattern>
    <rect width="290" height="100" fill="url(#dotGrid)"/>
    <rect x="266" y="100" width="24" height="182" fill="url(#dotGrid)"/>
  </svg>
  <div class="abs why-frame"></div>
  <div class="abs why-photo-b" role="img" aria-label="Two businessmen shaking hands across a table"></div>
  <h2 class="heading" style="left:690px;top:1778px">WHY CHOOSE</h2>
  <p class="para" style="left:694px;top:1867px;width:430px">Lorem ipsum dolor sit amet, consectetur adipis cing elit, sed do eiusmod tempor incididunt ut labore et dolore maorem ipsum dolor sit amet, consectetur adipiscing elit, sed do eiusmlorod tempor incididunt ut labore et dolore molorem ipsum dolor sit amet, consectetur adipis cing elit, sed do eiusmod tempor incididunt ut labore et dolore maorem ipsum dolor sit ame.</p>
  <div class="abs btn-outline">READ MORE</div>
</section>

<section>
  <h2 class="heading" style="left:134px;top:2542px">SOLUTIONS</h2>
  <p class="para" style="left:130px;top:2617px;width:545px">Lorem ipsum dolor sit amet, consectetur adipis cing elit, sed do eiusmod tempor incididunt ut labore et dolore maorem ipsum dolor sit amet, consectetur adipiscing elit, sed do eiu</p>

  <div class="sol-card" style="left:130px;background:linear-gradient(160deg,#dfe3e6 0%,#7b8a96 45%,#2f4b6e 100%)" role="img" aria-label="Hand holding a glass of water in a city setting">
    <div class="sol-caption"><h4>State Governments</h4><p>Lorem ipsum dolor sit amet consectetur adipiscing elited do eiusmod tempo.</p></div>
  </div>
  <div class="sol-card" style="left:424px;background:linear-gradient(160deg,#5a4a40 0%,#3a312c 50%,#8b6a4a 100%)" role="img" aria-label="Hand signing a document with a pen">
    <div class="sol-caption"><h4>Industries</h4><p>Lorem ipsum dolor sit amet consectetur adipiscing elited do eiusmod tempo.</p></div>
  </div>
  <div class="abs sol-big" role="img" aria-label="Hands on a laptop beneath floating scales of justice and legal icons">
    <div class="sol-caption"><h4>Other law firms, and individuals</h4><p>Lorem ipsum dolor sit amet consectetur adipiscing elited do eiusmod tempo.</p></div>
  </div>
</section>

<section>
  <svg class="abs" style="left:0;top:3255px" width="1200" height="466" viewBox="0 0 1200 466">
    <path d="M0 0H840A233 233 0 0 1 840 466H0Z" fill="#3a3a3a"/>
    <path d="M0 6H840A227 227 0 0 1 1067 233" fill="none" stroke="#c8874a" stroke-width="12"/>
    <path d="M0 6H840A227 227 0 0 1 1067 233" fill="none" stroke="#2b2b2b" stroke-width="2.5" stroke-dasharray="2 18"/>
  </svg>
  <div class="quote" style="left:130px;top:3348px">
    <div class="mark">&ldquo;</div>
    <p>&ldquo;Lorem ipsum dolor sit ametonetur adipis cing elit, sed do eiusoempor incididunt ut labore et doloreem ipsum dolor sit amet, consectetudip iscing elit, sed do eiusmlorod mpor inci didunt ut labore et doloorem ipsum dolor sit amet&rdquo;</p>
    <div class="name">Marla Quinn</div>
  </div>
  <div class="quote" style="left:526px;top:3348px">
    <div class="mark">&ldquo;</div>
    <p>&ldquo;Lorem ipsum dolor sit ametonetur adipis cing elit, sed do eiusoempor incididunt ut labore et doloreem ipsum dolor sit amet, consectetudip iscing elit, sed do eiusmlorod mpor inci didunt ut labore et doloorem ipsum dolor sit amet&rdquo;</p>
    <div class="name">Marla Quinn</div>
  </div>
</section>

<section>
  <div class="abs contact-scene" role="img" aria-label="Montana mountain lake valley with pine forest"></div>
  <h2 class="heading" style="left:0;width:1200px;text-align:center;top:3862px">CONTACT US TODAY</h2>
  <p class="para" style="left:300px;width:600px;text-align:center;top:3943px">Lorem ipsum dolor sit amet, consectetur adipis cing elit, sed do eiusmod tempor incididunt ut labore et dolore maorem</p>
  <div class="field" style="left:281px;top:4038px;width:311px">Name:</div>
  <div class="field" style="left:606px;top:4038px;width:311px">Email:</div>
  <div class="field" style="left:281px;top:4098px;width:311px">Phone:</div>
  <div class="field" style="left:606px;top:4098px;width:311px">Subject:</div>
  <div class="field msg" style="left:281px;top:4163px;width:636px;height:164px">Message</div>
  <div class="abs btn-submit">SUBMIT</div>
  <div class="abs location">
    <svg width="26" height="34" viewBox="0 0 26 34"><path d="M13 33C5 22 1 17 1 12a12 12 0 0 1 24 0c0 5-4 10-12 21z" fill="#d9c3a5"/><circle cx="13" cy="12" r="4.5" fill="#2b2b2b"/></svg>
    <span>OUR LOCATION IN MONTANA (U.S.A.)</span>
  </div>
</section>

<footer>
  <div class="abs footer"></div>
  <div class="info" style="left:296px">
    <span class="dot"><svg width="18" height="18" viewBox="0 0 24 24" fill="#fff"><path d="M6.6 10.8a15 15 0 0 0 6.6 6.6l2.2-2.2a1 1 0 0 1 1-.25 11.4 11.4 0 0 0 3.6.57 1 1 0 0 1 1 1V20a1 1 0 0 1-1 1A17 17 0 0 1 3 4a1 1 0 0 1 1-1h3.5a1 1 0 0 1 1 1c0 1.25.2 2.45.57 3.57a1 1 0 0 1-.25 1z"/></svg></span>
    <span>Phone<br>+00 5550 1842</span>
  </div>
  <div class="info" style="left:510px;top:4594px">
    <span class="dot"><svg width="18" height="14" viewBox="0 0 18 14" fill="#fff"><path d="M0 0h18v14H0z"/><path d="M0 0l9 7 9-7" fill="none" stroke="#d9c3a5" stroke-width="1.6"/></svg></span>
    <span>Email<br>info@lodgepole-law.com</span>
  </div>
  <div class="info" style="left:740px;top:4594px">
    <span class="dot"><svg width="16" height="20" viewBox="0 0 26 34"><path d="M13 33C5 22 1 17 1 12a12 12 0 0 1 24 0c0 5-4 10-12 21z" fill="#fff"/><circle cx="13" cy="12" r="4.5" fill="#d9c3a5"/></svg></span>
    <span>Ridgeway 12,<br>2600 Pinecrest</span>
  </div>
  <div class="abs bottom-bar"></div>
  <div class="abs copyright">COPYRIGHT © 2021 ALL RIGHT RESERVED</div>
  <div class="abs payment"><span>PAYMENT</span><strong>Quindle</strong></div>
</footer>

</body>
</html>
```